photowall advertisement

We require a wall featuring our company logo. We would like to avoid the color green, and gold is highly preferred. The design should be similar to the one in the attached photo. The wall will be used for photos and promotional purposes during congresses. Files must be prepared for printing.
dimension of wall: 470x223 cm

Industry/Entity Type

lifestyle

Colors
0054AA
0677BA
7BADD7
CADEEF
E8F1F8
6B429C
8869AF
B7A5CE
E3DAEB
F3F0F8

Requirements
Must have
• gold color, white, and other compare with gold color
Nice to have
• some pictograms, maps of Europe

```html
<!DOCTYPE html>
<html lang="en">
<head>
<meta charset="utf-8">
<title>Vela Arc Technology – Photo Wall</title>
<link rel="stylesheet" href="https://fonts.googleapis.com/css2?family=Michroma&display=swap">
<style>
  :root {
    --backdrop: #575757;
    --paper: #ffffff;
    --ink: #0b0b0b;
    --gold: #c9aa72;
    --tile-w: 67px;
    --tile-h: 48px;
  }
  * { box-sizing: border-box; margin: 0; padding: 0; }
  html, body { width: 936px; height: 1200px; overflow: hidden; }
  body {
    background: var(--backdrop);
    font-family: "Michroma", sans-serif;
    display: flex;
    align-items: center;
    justify-content: center;
  }
  .photo-wall {
    width: 740px;
    height: 351px;
    background: var(--paper);
    position: relative;
    overflow: hidden;
    box-shadow: 0 8px 24px rgba(0,0,0,.35);
  }
  .tile-band { position: absolute; left: 0; right: 0; }
  .tile-band--top { top: 0; }
  .tile-band--bottom { bottom: 0; }
  .tile-row { display: flex; height: var(--tile-h); }
  .tile-row--offset-a { margin-left: -58px; }
  .tile-row--offset-b { margin-left: -58px; }
  .tile-row--offset-c { margin-left: -48px; }
  .tile-row--offset-d { margin-left: -48px; }
  .tile {
    flex: 0 0 var(--tile-w);
    height: var(--tile-h);
    display: flex;
    align-items: center;
    justify-content: center;
    text-align: center;
  }
  .tile--name {
    background: var(--ink);
    color: var(--paper);
    font-size: 10px;
    line-height: 1.05;
  }
  .tile--initials {
    background: var(--paper);
    color: var(--gold);
    font-size: 23px;
    letter-spacing: -1px;
  }
  .wordmark {
    position: absolute;
    left: 0; right: 0;
    top: 152px;
    text-align: center;
    color: var(--ink);
  }
  .wordmark__name {
    font-size: 30px;
    letter-spacing: 2px;
    line-height: 1;
  }
  .wordmark__tagline {
    margin-top: 6px;
    font-size: 9px;
    letter-spacing: 7px;
  }
</style>
</head>
<body>
  <main class="photo-wall" aria-label="Vela Arc Technology photo wall, 470 × 223 cm">
    <div class="tile-band tile-band--top">
      <div class="tile-row tile-row--offset-a">
        <div class="tile tile--name">VELA<br>ARC</div><div class="tile tile--initials">VA</div>
        <div class="tile tile--name">VELA<br>ARC</div><div class="tile tile--initials">VA</div>
        <div class="tile tile--name">VELA<br>ARC</div><div class="tile tile--initials">VA</div>
        <div class="tile tile--name">VELA<br>ARC</div><div class="tile tile--initials">VA</div>
        <div class="tile tile--name">VELA<br>ARC</div><div class="tile tile--initials">VA</div>
        <div class="tile tile--name">VELA<br>ARC</div><div class="tile tile--initials">VA</div>
      </div>
      <div class="tile-row tile-row--offset-b">
        <div class="tile tile--initials">VA</div><div class="tile tile--name">VELA<br>ARC</div>
        <div class="tile tile--initials">VA</div><div class="tile tile--name">VELA<br>ARC</div>
        <div class="tile tile--initials">VA</div><div class="tile tile--name">VELA<br>ARC</div>
        <div class="tile tile--initials">VA</div><div class="tile tile--name">VELA<br>ARC</div>
        <div class="tile tile--initials">VA</div><div class="tile tile--name">VELA<br>ARC</div>
        <div class="tile tile--initials">VA</div><div class="tile tile--name">VELA<br>ARC</div>
      </div>
    </div>

    <div class="wordmark">
      <p class="wordmark__name">VELA ARC</p>
      <p class="wordmark__tagline">TECHNOLOGY</p>
    </div>

    <div class="tile-band tile-band--bottom">
      <div class="tile-row tile-row--offset-c">
        <div class="tile tile--name">VELA<br>ARC</div><div class="tile tile--initials">VA</div>
        <div class="tile tile--name">VELA<br>ARC</div><div class="tile tile--initials">VA</div>
        <div class="tile tile--name">VELA<br>ARC</div><div class="tile tile--initials">VA</div>
        <div class="tile tile--name">VELA<br>ARC</div><div class="tile tile--initials">VA</div>
        <div class="tile tile--name">VELA<br>ARC</div><div class="tile tile--initials">VA</div>
        <div class="tile tile--name">VELA<br>ARC</div><div class="tile tile--initials">VA</div>
      </div>
      <div class="tile-row tile-row--offset-d">
        <div class="tile tile--initials">VA</div><div class="tile tile--name">VELA<br>ARC</div>
        <div class="tile tile--initials">VA</div><div class="tile tile--name">VELA<br>ARC</div>
        <div class="tile tile--initials">VA</div><div class="tile tile--name">VELA<br>ARC</div>
        <div class="tile tile--initials">VA</div><div class="tile tile--name">VELA<br>ARC</div>
        <div class="tile tile--initials">VA</div><div class="tile tile--name">VELA<br>ARC</div>
        <div class="tile tile--initials">VA</div><div class="tile tile--name">VELA<br>ARC</div>
      </div>
    </div>
  </main>
</body>
</html>
```